In need of an AWESOME website for our Water Re-filling Store

The project is to design a website for our retail store front with the website www.brookvalefillhouse.com. Currently if you go to that site it redirects you to our other site www.brookvalebottleworks.com which is just our water bottle website. So, I need a new website created for www.brookvalefillhouse.com (retail storefront)
Use our Squarespace to create a site with pages to help educate, tell about us, link to our water bottle brand site that is already created with Squarespace, and show the family and community aspects that we believe in. Our current water bottle website is www.brookvalebottleworks.com for reference
We also sell hydration products, especially QRVX products and have access to digital media through our QRVX dealer site. we sell bottles, dispensers and other supplies for water refilling customers. We sell Ice as well.

Target Market(s)

Local residents looking to fill up their 1-5 gallon water jugs

Industry/Entity Type

Alkaline and Purified Water Retail Re-filling Store

Coding

Coded - Design and coding required

Font styles to use
Serif
Sans Serif

Colors
0054AA
0677BA
7BADD7
CADEEF
E8F1F8

Requirements
Must have
• pictures of our family in the about us section and pictures of our store inside and out.

```html
<!DOCTYPE html>
<html lang="en">
<head>
<meta charset="utf-8">
<title>Brookvale Fill House</title>
<link href="https://fonts.googleapis.com/css2?family=Antonio:wght@600;700&family=Roboto:wght@400;500&display=swap" rel="stylesheet">
<style>
:root{
  --blue-dark:#0054AA;
  --blue-mid:#0677BA;
  --blue-soft:#7BADD7;
  --blue-pale:#CADEEF;
  --blue-mist:#E8F1F8;
  --ink:#1d1d1f;
  --grey:#5e6670;
  --hero-bg:#ebecec;
  --white:#ffffff;
}
*{margin:0;padding:0;box-sizing:border-box}
html,body{width:1200px;height:3547px;overflow:hidden}
body{position:relative;background:var(--white);font-family:"Roboto",sans-serif;color:var(--ink)}
.abs{position:absolute}
.head-font{font-family:"Antonio",sans-serif;font-weight:700;text-transform:uppercase;letter-spacing:.5px;color:var(--blue-dark);line-height:1.04}
.btn{display:flex;align-items:center;justify-content:center;border-radius:24px;font-size:15px;font-weight:500;height:44px;text-decoration:none}
.abs-btn{position:absolute}
.btn-solid{background:var(--blue-dark);color:var(--white)}
.btn-ghost{background:var(--white);color:var(--blue-dark)}

/* hero */
.hero-bg{left:0;top:0;width:1200px;height:820px;background:var(--hero-bg)}
.hero-photo{left:550px;top:60px;width:650px;height:680px;background:linear-gradient(180deg,#dfe6ee 0%,#3a3d44 35%,#2b2e33 70%,#d9dde2 100%)}
.brand{left:100px;top:42px;width:195px;text-align:center;font-weight:500;color:var(--blue-dark)}
.brand-mark{width:26px;height:26px;border-radius:50%;background:var(--blue-mid);margin:0 auto 8px}
.brand-name{font-size:19px;line-height:1.15;white-space:nowrap}
.brand-phone{font-size:14px;margin-top:4px}
.nav{left:443px;top:36px;display:flex;gap:40px;font-size:14px;font-weight:500;color:#222}
.hero-title{left:110px;top:228px}
.hero-title .small{font-size:58px;color:#111;display:block}
.hero-title .big{font-size:76px;display:block;margin-top:2px}
.hero-text{left:112px;top:370px;width:400px;font-size:21px;line-height:33px;color:#333}

/* products */
.products-bg{left:0;top:820px;width:1200px;height:760px;background:var(--blue-mist)}
.sec-title{left:0;width:1200px;text-align:center;font-size:56px}
.sec-sub{left:0;width:1200px;text-align:center;top:977px;font-size:16px;line-height:26px;color:var(--grey)}
.card{position:absolute;top:1063px;width:233px;height:329px;background:var(--white);border-radius:14px;overflow:hidden;box-shadow:0 2px 8px rgba(0,50,120,.08)}
.card-img{height:276px}
.card-foot{display:flex;justify-content:space-between;align-items:center;padding:0 18px;height:53px;font-size:15px;font-weight:500}
.card-arrow{width:26px;height:26px;border-radius:50%;background:var(--blue-dark);display:flex;align-items:center;justify-content:center}

/* story */
.story-ring{left:110px;top:1730px;width:490px;height:490px;border-radius:50%;border:3px solid var(--blue-mid);background:var(--white);box-shadow:0 0 30px rgba(0,84,170,.12)}
.story-photo{left:150px;top:1770px;width:410px;height:410px;border-radius:50%;background:linear-gradient(180deg,#cfd3d0 0%,#bfb8a8 55%,#a39c8d 100%)}
.story-block{left:680px;top:1758px;width:410px}
.story-block h2{font-size:56px;margin-bottom:14px}
.body-copy{font-size:15px;line-height:31px;color:var(--grey);text-align:justify}
.story-block .btn{width:146px;margin-top:28px}

/* bottles */
.bottles-block{left:110px;top:2375px;width:412px}
.bottles-block h2{font-size:56px;margin-bottom:12px}
.plain-copy{font-size:15.5px;line-height:27px;color:var(--grey)}
.ticks{list-style:none;font-size:15.5px;font-weight:500;color:#222;margin:16px 0 16px 28px}
.ticks li{display:flex;align-items:center;gap:12px;height:31px}
.tick{width:16px;height:16px;border-radius:4px;background:var(--blue-dark);display:flex;align-items:center;justify-content:center}
.bottles-block .btn{width:147px;margin-top:18px}
.bottles-photo{left:600px;top:2357px;width:490px;height:490px;border-radius:50%;background:linear-gradient(180deg,#8b8378 0%,#6f7d8f 40%,#e9edf2 70%,#f4f6f8 100%)}

/* footer */
.foot-brand{left:90px;top:3200px;width:320px;text-align:center;color:var(--white);font-weight:500}
.foot-brand .brand-mark{width:40px;height:40px;background:var(--white);margin-bottom:14px}
.foot-brand .brand-name{font-size:30px;line-height:1.1}
.foot-brand .brand-phone{font-size:24px;margin-top:10px}
.foot-col{top:3185px;color:var(--white)}
.foot-col h3{font-family:"Antonio",sans-serif;font-weight:600;font-size:27px;text-transform:uppercase;margin-bottom:12px}
.foot-col ul{list-style:none}
.foot-col li{display:flex;align-items:center;gap:22px;font-size:16px;height:36px}
.chev{font-size:14px}
.social{display:flex;gap:9px}
.social span{width:34px;height:34px;border-radius:50%;background:var(--white);display:flex;align-items:center;justify-content:center}
.social span i{width:8px;height:8px;border-radius:50%;background:var(--blue-dark);display:block}
.foot-rule{left:110px;top:3450px;width:980px;border-top:1px dashed rgba(255,255,255,.6)}
.copyright{left:0;top:3508px;width:1200px;text-align:center;color:var(--white);font-size:12px}
</style>
</head>
<body>

<!-- hero -->
<div class="abs hero-bg"></div>
<div class="abs hero-photo" role="img" aria-label="Store interior wall with water jugs on a top shelf and reusable bottles and tumblers on slatwall displays"></div>
<svg class="abs" style="left:0;top:0" width="1200" height="820" viewBox="0 0 1200 820">
  <path d="M0,700 C200,660 400,680 620,765 C800,825 1000,800 1200,640 L1200,820 L0,820Z" fill="#E8F1F8"/>
  <path d="M40,680 C250,600 420,630 620,720 C800,800 1000,780 1200,610 L1200,640 C1000,805 800,830 620,765 C430,690 250,650 40,680Z" fill="#0054AA"/>
</svg>

<div class="abs brand">
  <div class="brand-mark"></div>
  <div class="brand-name">Brookvale Fill House</div>
  <div class="brand-phone">555-014-2290</div>
</div>
<nav class="abs nav"><span>Home</span><span>About Us</span><span>Hydration 101</span><span>Products &amp; Services</span><span>Community</span><span>Visit Us</span></nav>

<h1 class="abs hero-title head-font"><span class="small">Your Local</span><span class="big">Fill House</span></h1>
<p class="abs hero-text">Clean water, electrolytes, ice, and refill essentials - everything you need to stay hydrated every day.</p>
<a class="btn abs-btn btn-solid" style="left:111px;top:490px;width:168px">Visit Our Store</a>
<a class="btn abs-btn btn-ghost" style="left:294px;top:490px;width:168px">Explore Products</a>

<!-- products -->
<div class="abs products-bg"></div>
<svg class="abs" style="left:0;top:1440px" width="1200" height="200" viewBox="0 0 1200 200">
  <path d="M0,87 C250,70 450,140 700,180 C950,210 1100,90 1200,10 L1200,200 L0,200Z" fill="#ffffff"/>
</svg>
<h2 class="abs sec-title head-font" style="top:856px">Products That Support Your<br>Daily Hydration</h2>
<p class="abs sec-sub">We've carefully selected products that make staying hydrated easier, more<br>affordable, and more effective.</p>

<div class="card" style="left:110px">
  <div class="card-img" role="img" aria-label="Ice freezer filled with bagged ice" style="background:linear-gradient(180deg,#9fc4e8,#e6ecf2 40%,#c9d3dc)"></div>
  <div class="card-foot">Fresh Ice Bag<span class="card-arrow"><svg width="12" height="12" viewBox="0 0 12 12"><path d="M1 6h9M6 2l4 4-4 4" stroke="#fff" stroke-width="1.6" fill="none"/></svg></span></div>
</div>
<div class="card" style="left:358px">
  <div class="card-img" role="img" aria-label="Three five-gallon water jugs with splashing water" style="background:linear-gradient(180deg,#eef5fb,#9cc3e6 60%,#eef5fb)"></div>
  <div class="card-foot">Water Refill<span class="card-arrow"><svg width="12" height="12" viewBox="0 0 12 12"><path d="M1 6h9M6 2l4 4-4 4" stroke="#fff" stroke-width="1.6" fill="none"/></svg></span></div>
</div>
<div class="card" style="left:607px">
  <div class="card-img" role="img" aria-label="Cooler shelves stocked with electrolyte drink cans" style="background:linear-gradient(180deg,#4a4f55,#a78a84 50%,#8c9a98)"></div>
  <div class="card-foot">QRVX Electrolyte Pack<span class="card-arrow"><svg width="12" height="12" viewBox="0 0 12 12"><path d="M1 6h9M6 2l4 4-4 4" stroke="#fff" stroke-width="1.6" fill="none"/></svg></span></div>
</div>
<div class="card" style="left:856px">
  <div class="card-img" role="img" aria-label="Kombucha cans on a store shelf" style="background:linear-gradient(180deg,#c9ccd0,#3a4d78 50%,#5a6478)"></div>
  <div class="card-foot">Kombucha<span class="card-arrow"><svg width="12" height="12" viewBox="0 0 12 12"><path d="M1 6h9M6 2l4 4-4 4" stroke="#fff" stroke-width="1.6" fill="none"/></svg></span></div>
</div>
<a class="btn abs-btn btn-solid" style="left:509px;top:1436px;width:181px">Explore Products</a>

<!-- story -->
<div class="abs story-ring"></div>
<div class="abs story-photo" role="img" aria-label="Family of seven standing together on a beach"></div>
<div class="abs story-block">
  <h2 class="head-font">Our Story</h2>
  <div class="body-copy">
    <p>At Brookvale Fill Co., hydration goes far beyond simply quenching thirst; it represents a deep commitment to enhancing both personal health and environmental sustainability.</p>
    <p style="margin-top:30px">Drawing inspiration from the resilient and vibrant spirit of Sonora Valley, the brand delivers a premium alkaline water experience thoughtfully designed to meet the needs of today's health-conscious and eco-aware consumers.</p>
  </div>
  <a class="btn btn-solid">Explore More</a>
</div>

<!-- bottles -->
<div class="abs bottles-block">
  <h2 class="head-font">Bottles &amp; Hydration<br>Supplies</h2>
  <p class="plain-copy">We offer durable bottles, dispensers, and hydration tools designed to make refilling and storing water simple and convenient.</p>
  <ul class="ticks">
    <li><span class="tick"><svg width="10" height="10" viewBox="0 0 10 10"><path d="M1.5 5l2.5 2.5 4.5-5" stroke="#fff" stroke-width="1.6" fill="none"/></svg></span>Reusable and long-lasting</li>
    <li><span class="tick"><svg width="10" height="10" viewBox="0 0 10 10"><path d="M1.5 5l2.5 2.5 4.5-5" stroke="#fff" stroke-width="1.6" fill="none"/></svg></span>Easy to clean and maintain</li>
    <li><span class="tick"><svg width="10" height="10" viewBox="0 0 10 10"><path d="M1.5 5l2.5 2.5 4.5-5" stroke="#fff" stroke-width="1.6" fill="none"/></svg></span>Ideal for home, work, or on the go</li>
  </ul>
  <p class="plain-copy">Whether you're setting up your home system or upgrading your routine, we've got practical solutions that work.</p>
  <a class="btn btn-solid">View Product</a>
</div>
<div class="abs bottles-photo" role="img" aria-label="Two store owners standing behind rows of packaged water bottles"></div>

<!-- footer -->
<svg class="abs" style="left:0;top:2940px" width="1200" height="607" viewBox="0 0 1200 607">
  <path d="M28,170 C250,40 450,0 650,60 C850,120 1000,130 1200,110 L1200,607 L0,607 L0,190Z" fill="#0677BA"/>
  <path d="M0,190 C200,80 420,70 640,130 C850,185 1000,170 1200,125 L1200,607 L0,607Z" fill="#0054AA"/>
  <path d="M28,170 C230,70 430,60 640,125 C850,180 1000,165 1200,120 L1200,128 C1000,176 850,192 640,138 C430,80 230,90 28,178Z" fill="#ffffff"/>
</svg>

<div class="abs foot-brand">
  <div class="brand-mark"></div>
  <div class="brand-name">Brookvale Fill House</div>
  <div class="brand-phone">555-014-2290</div>
</div>

<div class="abs foot-col" style="left:463px">
  <h3>Quick Links</h3>
  <ul>
    <li><span class="chev">&raquo;</span>Home</li>
    <li><span class="chev">&raquo;</span>About Us</li>
    <li><span class="chev">&raquo;</span>Hydration 101</li>
    <li><span class="chev">&raquo;</span>Products &amp; Services</li>
    <li><span class="chev">&raquo;</span>Community</li>
    <li><span class="chev">&raquo;</span>Visit Us</li>
  </ul>
</div>
<div class="abs foot-col" style="left:712px">
  <h3>Help Links</h3>
  <ul>
    <li><span class="chev">&raquo;</span>Help</li>
    <li><span class="chev">&raquo;</span>Support</li>
    <li><span class="chev">&raquo;</span>Privacy Policy</li>
    <li><span class="chev">&raquo;</span>Terms &amp; Conditions</li>
    <li><span class="chev">&raquo;</span>Return Policy</li>
    <li><span class="chev">&raquo;</span>Contact Us</li>
  </ul>
</div>
<div class="abs foot-col" style="left:950px">
  <h3>Let's Connect</h3>
  <div class="social"><span><i></i></span><span><i></i></span><span><i></i></span></div>
</div>

<div class="abs foot-rule"></div>
<p class="abs copyright">(C) Copyright 2026 | All Rights Reserved</p>

</body>
</html>
```